Willow Harbor Family Relief-buis card/stationary design for our non profit company
Have fun, be creative and lets see what you come up with!
Willow Harbor Family Relief-buis card/stationary design for our non profit company - Health
Creative Brief
Bright & Fun-filled
Dana Holloway
27415 Marlow Ave Ste#208 Tustin CA 92781
harborwr@brightpostmail.net
We have not yet decided our titles yet. In the meantime please focus on the design. Once we choose the design we want, we will ask you to put our names,title etc. Thank you!
Please put our tagline: "Supporting the care in caregiving" on the back of the card.

```html
<!DOCTYPE html>
<html lang="en">
<head>
<meta charset="utf-8">
<title>Willow Harbor Family Relief – Business Card</title>
<link rel="stylesheet" href="https://fonts.googleapis.com/css2?family=Cinzel:wght@600&family=Oswald:wght@500&family=Roboto:wght@400;500&display=swap">
<style>
  :root {
    --page-bg: #e6e3df;
    --card-top: #f4f5f7;
    --card-bottom: #d9dce0;
    --brand-blue: #1f4fa8;
    --brand-blue-dark: #173f8c;
    --icon-fill: #e9edf3;
    --ink-light: #ffffff;
    --ink-soft: #d7e1f2;
    --ink-grey: #5d6168;
    --social-grey: #6f737a;
  }
  * { box-sizing: border-box; margin: 0; padding: 0; }
  html, body {
    width: 1200px; height: 768px; overflow: hidden;
    background: var(--page-bg);
  }
  .business-card {
    position: absolute; left: 110px; top: 85px;
    width: 980px; height: 598px;
    border-radius: 12px; overflow: hidden;
    background: linear-gradient(180deg, var(--card-top) 0%, #e8eaee 55%, var(--card-bottom) 100%);
    box-shadow: 0 18px 40px rgba(0,0,0,0.18);
  }
  .brand-lockup {
    position: absolute; left: 286px; top: 58px;
    display: flex; align-items: center; gap: 26px;
  }
  .brand-disc {
    width: 96px; height: 96px; border-radius: 50%;
    background: var(--brand-blue);
  }
  .brand-name {
    font-family: "Cinzel", serif; font-weight: 600;
    color: var(--brand-blue); line-height: 1.1;
  }
  .brand-name .line-one { display: block; font-size: 40px; letter-spacing: 1px; }
  .brand-name .line-two { display: block; font-size: 26px; letter-spacing: 3px; text-align: center; }
  .contact-band {
    position: absolute; left: 0; top: 198px; width: 100%; height: 274px;
    background: linear-gradient(180deg, var(--brand-blue) 0%, var(--brand-blue-dark) 100%);
  }
  .contact-column {
    position: absolute; top: 36px;
    display: flex; flex-direction: column; align-items: center;
    transform: translateX(-50%);
    color: var(--ink-light); text-align: center;
    white-space: nowrap;
  }
  .contact-column.person { left: 188px; }
  .contact-column.web { left: 492px; }
  .contact-column.phone { left: 803px; }
  .icon-disc {
    width: 90px; height: 90px; border-radius: 50%;
    background: var(--icon-fill);
    display: flex; align-items: center; justify-content: center;
    margin-bottom: 30px;
  }
  .person-name {
    font-family: "Oswald", sans-serif; font-weight: 500;
    font-size: 33px; letter-spacing: 1px; line-height: 1.1;
    text-transform: uppercase;
  }
  .person-title {
    font-family: "Roboto", sans-serif; font-size: 12px;
    letter-spacing: 2px; text-transform: uppercase; color: var(--ink-soft);
    margin-top: 2px;
  }
  .contact-lines {
    font-family: "Roboto", sans-serif; font-size: 20px;
    line-height: 32px; letter-spacing: 0.5px; margin-top: 2px;
  }
  .social-row {
    position: absolute; left: 90px; top: 505px;
    display: flex; align-items: center; gap: 44px;
  }
  .follow-label {
    font-family: "Roboto", sans-serif; color: var(--ink-grey);
  }
  .follow-label .main { display: block; font-size: 26px; font-weight: 500; letter-spacing: 2px; }
  .follow-label .sub { display: block; font-size: 11px; letter-spacing: 2px; }
  .social-marks { display: flex; gap: 22px; }
  .social-mark {
    width: 30px; height: 30px; border-radius: 4px;
    background: var(--social-grey);
  }
</style>
</head>
<body>
  <main class="business-card">
    <header class="brand-lockup">
      <div class="brand-disc"></div>
      <div class="brand-name">
        <span class="line-one">Willow Harbor</span>
        <span class="line-two">Family Relief</span>
      </div>
    </header>

    <section class="contact-band">
      <div class="contact-column person">
        <div class="icon-disc">
          <svg width="50" height="50" viewBox="0 0 50 50" aria-hidden="true">
            <circle cx="25" cy="17" r="9" fill="#1f4fa8"/>
            <path d="M8 44 C8 32 16 28 25 28 C34 28 42 32 42 44 Z" fill="#1f4fa8"/>
          </svg>
        </div>
        <div class="person-name">Dana Holloway</div>
        <div class="person-title">General Manager</div>
      </div>

      <div class="contact-column web">
        <div class="icon-disc">
          <svg width="54" height="54" viewBox="0 0 54 54" aria-hidden="true">
            <g fill="none" stroke="#1f4fa8" stroke-width="3">
              <circle cx="27" cy="27" r="22"/>
              <ellipse cx="27" cy="27" rx="10" ry="22"/>
              <line x1="5" y1="27" x2="49" y2="27"/>
              <path d="M9 16 H45 M9 38 H45"/>
            </g>
          </svg>
        </div>
        <div class="contact-lines">
          <div>harborwr@brightpostmail.net</div>
          <div>www.willowharborrelief.org</div>
        </div>
      </div>

      <div class="contact-column phone">
        <div class="icon-disc">
          <svg width="40" height="54" viewBox="0 0 40 54" aria-hidden="true">
            <rect x="6" y="3" width="28" height="48" rx="5" fill="none" stroke="#1f4fa8" stroke-width="3.5"/>
            <line x1="10" y1="40" x2="30" y2="40" stroke="#1f4fa8" stroke-width="2"/>
            <circle cx="20" cy="45" r="2.3" fill="#1f4fa8"/>
          </svg>
        </div>
        <div class="contact-lines">
          <div>555 014 2207</div>
          <div>555 014 2208</div>
        </div>
      </div>
    </section>

    <footer class="social-row">
      <div class="follow-label">
        <span class="main">FOLLOW US</span>
        <span class="sub">ON SOCIAL NETWORKS</span>
      </div>
      <div class="social-marks">
        <div class="social-mark"></div>
        <div class="social-mark"></div>
        <div class="social-mark"></div>
        <div class="social-mark"></div>
      </div>
    </footer>
  </main>
</body>
</html>
```